Velmora Intergrated Marketing Stationary Design Contest

We require a very professional looking stationary set to include: letterhead, compliments slip and business cards (double sided bus cards).

Files should be supplied on either Illustrator or InDesign.

We are interested in perhaps encorporating a faint watermark with the letter q or the logo, but it isnt a pre-requisite

Target Market(s)

Business owners seeking professional marketing services

Industry/Entity Type

Marketing

Requirements
Must have
• Concurrent theme wiht business cards, letterhead and comp slip. Must be an editable document for future ammendment
Should not have
• No use of times new roman or similar fonts

```html
<!DOCTYPE html>
<html lang="en">
<head>
<meta charset="utf-8">
<title>Velmora Intergrated Marketing – Stationery Set</title>
<link href="https://fonts.googleapis.com/css2?family=Arimo:ital,wght@0,400;0,700;1,400&family=Questrial&display=swap" rel="stylesheet">
<style>
  :root {
    --orange: #ef5a24;
    --slate: #313b42;
    --paper: #ffffff;
    --ink: #2a3237;
    --band-text: #ffffff;
    --canvas: #ffffff;
  }
  * { box-sizing: border-box; margin: 0; padding: 0; }
  html, body { width: 1200px; height: 1200px; overflow: hidden; background: var(--canvas); }
  body { position: relative; font-family: "Arimo", Arial, sans-serif; color: var(--ink); }

  .sheet { position: absolute; background: var(--paper); box-shadow: 0 1px 4px rgba(0,0,0,.28); overflow: hidden; }

  .brand-name { position: absolute; font-family: "Questrial", sans-serif; color: var(--slate);
                letter-spacing: .06em; line-height: 1; white-space: nowrap; }

  .address { position: absolute; text-align: right; line-height: 1.2; }
  .address .company { color: var(--orange); }

  .band { position: absolute; left: 0; right: 0; background: var(--slate); color: var(--band-text);
          display: flex; align-items: center; justify-content: space-between; }
  .label { color: var(--orange); }

  /* Letterhead */
  .letterhead { left: 203px; top: 37px; width: 794px; height: 1123px; }
  .letterhead .head { position: absolute; left: 0; top: 0; width: 100%; height: 139px;
                      background: radial-gradient(ellipse at 30% 20%, #fafafa 0%, #efeff0 55%, #e4e5e6 100%); }
  .letterhead .brand-name { left: 24px; top: 35px; font-size: 46px; }
  .letterhead .address { right: 19px; top: 7px; font-size: 14px; line-height: 16.6px; }
  .letterhead .address .company { font-size: 17px; line-height: 20px; }
  .letterhead .contact-band { top: 139px; height: 36px; padding: 0 15px; font-size: 14px; }
  .letterhead .legal-band { bottom: 0; height: 36px; padding: 0 20px; font-size: 13px; }

  /* Compliments slip */
  .comp-slip { left: 53px; top: 646px; width: 795px; height: 374px;
               background: radial-gradient(ellipse at 35% 40%, #ffffff 0%, #eeeeef 55%, #e3e4e5 100%); }
  .comp-slip .brand-name { left: 24px; top: 30px; font-size: 46px; }
  .comp-slip .address { right: 19px; top: 20px; font-size: 16px; line-height: 18px; }
  .comp-slip .address .company { font-size: 18px; line-height: 22px; }
  .comp-slip .greeting { position: absolute; left: 37px; top: 120px; font-style: italic; font-size: 18px; }
  .comp-slip .contacts { position: absolute; right: 19px; top: 262px; text-align: right; font-size: 15px; line-height: 18px; }
  .comp-slip .legal-band { bottom: 0; height: 36px; padding: 0 20px; font-size: 13px; }

  /* Business cards */
  .card { top: 309px; width: 321px; height: 207px; }
  .card-front { left: 496px; background: radial-gradient(ellipse at 30% 30%, #3a454c 0%, var(--slate) 70%); }
  .card-front .brand-name { left: 28px; top: 84px; font-size: 32px; color: #e8eaeb; }

  .card-back { left: 840px; background: linear-gradient(180deg, #f7f7f8, #e8e9ea); }
  .card-back .side { position: absolute; left: 0; top: 0; width: 119px; height: 100%; background: var(--slate); }
  .card-back .person { position: absolute; left: 12px; top: 51px; color: #fff; font-size: 14px; line-height: 1.15; }
  .card-back .person .role { color: var(--orange); font-size: 12px; }
  .card-back .address { right: 13px; top: 13px; font-size: 10.5px; line-height: 12.4px; }
  .card-back .address .company { font-size: 12.5px; line-height: 14px; }
  .card-back .contacts { position: absolute; right: 13px; top: 144px; text-align: right; font-size: 10.5px; line-height: 12.4px; }
</style>
</head>
<body>

  <!-- Letterhead -->
  <section class="sheet letterhead" aria-label="Letterhead">
    <div class="head">
      <div class="brand-name">velmora</div>
      <div class="address">
        <div class="company">Velmora Intergrated Marketing</div>
        <div>Main Offices</div><div>Harbour Street</div><div>Kelbrook</div><div>North Yorkshire</div><div>KB14 3QT</div>
      </div>
    </div>
    <div class="band contact-band">
      <span><span class="label">tel:</span>&nbsp; 01632 960614</span>
      <span><span class="label">fax:</span>&nbsp; 01632 960611</span>
      <span><span class="label">web:</span>&nbsp; www.velmoraim.co.uk</span>
      <span><span class="label">email:</span>&nbsp; daniel@velmoraim.co.uk</span>
    </div>
    <div class="band legal-band">
      <span>Company registration&nbsp; <span class="label">4813705</span></span>
      <span>Vat No&nbsp; <span class="label">718 2045 36</span></span>
      <span>Trading as a division of Brantwell Ltd</span>
    </div>
  </section>

  <!-- Business card front -->
  <section class="sheet card card-front" aria-label="Business card front">
    <div class="brand-name">velmora</div>
  </section>

  <!-- Business card back -->
  <section class="sheet card card-back" aria-label="Business card back">
    <div class="side">
      <div class="person"><div>Daniel Hartley</div><div class="role">General Manager</div></div>
    </div>
    <div class="address">
      <div class="company">Velmora Intergrated Marketing</div>
      <div>Main Offices</div><div>Harbour Street</div><div>Kelbrook</div><div>North Yorkshire</div><div>KB14 3QT</div>
    </div>
    <div class="contacts">
      <div><span class="label">tel:</span> 01632 960614</div>
      <div><span class="label">fax:</span> 01632 960611</div>
      <div><span class="label">web:</span> www.velmoraim.co.uk</div>
      <div><span class="label">email:</span> daniel@velmoraim.co.uk</div>
    </div>
  </section>

  <!-- Compliments slip -->
  <section class="sheet comp-slip" aria-label="Compliments slip">
    <div class="brand-name">velmora</div>
    <div class="greeting">with compliments</div>
    <div class="address">
      <div class="company">Velmora Intergrated Marketing</div>
      <div>Main Offices</div><div>Harbour Street</div><div>Kelbrook</div><div>North Yorkshire</div><div>KB14 3QT</div>
    </div>
    <div class="contacts">
      <div><span class="label">tel:</span>&nbsp; 01632 960614</div>
      <div><span class="label">fax:</span>&nbsp; 01632 960611</div>
      <div><span class="label">web:</span>&nbsp; www.velmoraim.co.uk</div>
      <div><span class="label">email:</span>&nbsp; daniel@velmoraim.co.uk</div>
    </div>
    <div class="band legal-band">
      <span>Company registration&nbsp; <span class="label">4813705</span></span>
      <span>Vat No&nbsp; <span class="label">718 2045 36</span></span>
      <span>Trading as a division of Brantwell Ltd</span>
    </div>
  </section>

</body>
</html>
```